Marlow & Tate
Business card and stationery design for a management consulting firm  - Consulting
Simple
Benedikt Owen Dolsquin
Lead Consultant
Njegoševa 47 11000 Belgrade
benedikt.owen@marlowtate-example.com
www.marlowtate-example.com
Keep the design clean. "Scandinavian design approach". Address line on business card is preferred not to be included, although if designer finds it to complete the holistic 'picture' of the card, then he/she may use it. Font selection for the rest of the text is up to the designer. Although please note that the font has to be in balance with the logo. Business cards are to be printed on black paper / metal. If printed on paper, the logo part will be with relief printing.
This is designers choice to be creative
dolsquin dolsquin
Tip to designers: Try not to use the monogram "MT" with "Marlow and Tate" on the same side. Printing techniques that will be used are: Embossing / Debossing, Thermography. Keep it clean. Less is more.

```html
<!DOCTYPE html>
<html lang="en">
<head>
<meta charset="UTF-8">
<title>Marlow &amp; Tate — Business Card</title>
<link href="https://fonts.googleapis.com/css2?family=Raleway:wght@300;400;500&display=swap" rel="stylesheet">
<style>
  :root {
    --backdrop: #a4a4a4;
    --card-top: #2c2c2c;
    --card-bottom: #191919;
    --ink-light: #e6e6e6;
    --ink-mid: #a9a9a9;
    --ink-soft: #7d7d7d;
    --rule: #5a5a5a;
    --relief: #0e0e0e;
    --label: #111111;
  }
  * { margin: 0; padding: 0; box-sizing: border-box; }
  html, body {
    width: 1200px;
    height: 925px;
    overflow: hidden;
    background: var(--backdrop);
    font-family: "Raleway", "Helvetica Neue", Arial, sans-serif;
  }
  .sheet {
    width: 1200px;
    height: 925px;
    display: flex;
    justify-content: center;
    align-items: center;
    gap: 44px;
  }
  .side {
    display: flex;
    flex-direction: column;
    align-items: center;
    gap: 34px;
  }
  .card {
    width: 540px;
    height: 312px;
    background: linear-gradient(160deg, var(--card-top), var(--card-bottom));
    box-shadow: 0 2px 6px rgba(0,0,0,.25);
    position: relative;
    display: flex;
    flex-direction: column;
    align-items: center;
    color: var(--ink-light);
  }
  .brand {
    margin-top: 82px;
    font-weight: 300;
    font-size: 34px;
    letter-spacing: 1px;
    color: var(--relief);
    text-shadow: 0 1px 0 rgba(255,255,255,.14);
  }
  .holder {
    margin-top: 44px;
    font-size: 15px;
    font-weight: 500;
    color: var(--ink-light);
  }
  .holder .role { font-weight: 400; color: var(--ink-mid); }
  .holder .divider { color: var(--ink-soft); margin: 0 8px; }
  .rule {
    width: 340px;
    height: 1px;
    background: var(--rule);
    margin-top: 16px;
  }
  .contact {
    margin-top: 14px;
    font-size: 11px;
    color: var(--ink-mid);
  }
  .contact .divider { margin: 0 6px; color: var(--ink-soft); }
  .website {
    margin-top: 14px;
    font-size: 11px;
    color: var(--ink-soft);
  }
  .monogram {
    margin-top: 104px;
    font-weight: 300;
    font-size: 68px;
    letter-spacing: 4px;
    color: var(--relief);
    text-shadow: 0 1px 0 rgba(255,255,255,.16);
  }
  .card--back .website {
    position: absolute;
    bottom: 30px;
    margin: 0;
  }
  .side-label {
    font-size: 28px;
    font-weight: 400;
    color: var(--label);
  }
</style>
</head>
<body>
  <main class="sheet">
    <section class="side">
      <article class="card card--front">
        <div class="brand">Marlow and Tate</div>
        <p class="holder">Benedikt Owen Dolsquin<span class="divider">|</span><span class="role">Lead Consultant</span></p>
        <div class="rule"></div>
        <p class="contact">+381 60 555 0142<span class="divider">|</span>benedikt.owen@marlowtate-example.com</p>
        <p class="website">www.marlowtate-example.com</p>
      </article>
      <h2 class="side-label">Front</h2>
    </section>
    <section class="side">
      <article class="card card--back">
        <div class="monogram">MT</div>
        <p class="website">www.marlowtate-example.com</p>
      </article>
      <h2 class="side-label">Back</h2>
    </section>
  </main>
</body>
</html>
```